New Company Logo & Responsive Website Design for Codeweave Orchard

Codeweave Orchard provides a white labeled, digital lending platform technology solutions to the mortgage industry via a SaaS model. Our target market is Mortgage Companies and Banks who are looking for innovative technology to assist both borrowers and loan originators with the lending process, while automating as much of he process as possible.

Codeweave Orchard is our company name, and our modular software offerings Include the following Products:

1) Applicant Orchard: A customizable, web based, point-of-sale application for borrowers to complete a loan application, and guide them through the mortgage process.

POS Definition
"A point of sale (POS) is the client-facing software solution that allows borrowers to create a customer portal, apply for a loan online, and seamlessly submit needed documentation."

2) Escrowmap Orchard: A Mortgage Loan Origination System

LOS Definition
"A Mortgage Loan Origination System (LOS) is a platform that takes a completed loan application and facilitates the mortgage transaction from origination to post closing. LOS systems may include document management, pricing and eligibility engines, and compliance tools to decrease risk and increase loan manufacturing quality.

3) Dwelling Orchard: A brandable, home search website

The LOS and POS definitions provided above are just for your understanding of what these products are, not to be included word-for-word as website content.

We are looking for designs that are elegant, convey technical competency, simple to navigate, and set us apart from the competition.

We are not set on any particular colors at this point, so feel free to choose the best colors for your particular designs.

Please include company logo, both desktop and mobile designs with a template design for the website sub pages.

Some Examples of Mortgage Technology Websites offering similar products. These are to show the typical content, not designs that we particularly like or dislike.

https://trenvask.com/
https://www.brightquorel.com/
https://www.dwelfundbuddy.com/
https://www.escrowotter.com/
https://www.quennidata.com/products/route

Please send comments with additional questions.

Thank You For your participation.

```html
<!DOCTYPE html>
<html lang="en">
<head>
<meta charset="utf-8">
<title>Codeweave Orchard</title>
<link href="https://fonts.googleapis.com/css2?family=Ubuntu:wght@400;500;700&family=Montserrat:wght@500;700&family=Lato:wght@400;700&family=Roboto+Slab:wght@300;400&display=swap" rel="stylesheet">
<style>
:root{
  --navy:#0b4a8f;
  --navy-deep:#083f7c;
  --red:#ee1c24;
  --ink:#111;
  --text:#555;
  --muted:#777;
  --soft:#f3f4f6;
  --ring:#6f8fd8;
  --white:#fff;
}
*{margin:0;padding:0;box-sizing:border-box}
html,body{width:1200px;height:3996px;overflow:hidden;background:var(--white)}
body{position:relative;font-family:'Lato',sans-serif;color:var(--text)}
.abs{position:absolute}
.hero-bg{position:absolute;left:0;top:0}
.brand{position:absolute;left:98px;top:18px;font-family:'Ubuntu',sans-serif;font-weight:700;font-size:30px;color:var(--white)}
.nav{position:absolute;top:31px;font-family:'Lato',sans-serif;font-size:15.5px;color:var(--white)}
.nav .caret{font-size:10px;margin-left:3px}
.btn{position:absolute;display:flex;align-items:center;justify-content:center;background:var(--red);color:var(--white);border-radius:8px;font-family:'Ubuntu',sans-serif;font-weight:500}
.btn-login{left:940px;top:16px;width:145px;height:49px;border-radius:25px;font-family:'Lato',sans-serif;font-weight:700;font-size:19px;border:2px solid #ff5a5a}
.hero-kicker{position:absolute;left:0;width:1200px;top:138px;text-align:center;font-family:'Montserrat',sans-serif;font-weight:500;font-size:34px;color:var(--white)}
.hero-title{position:absolute;left:0;width:1200px;top:180px;text-align:center;font-family:'Montserrat',sans-serif;font-weight:700;font-size:72px;color:var(--white);letter-spacing:1px}
.hero-text{position:absolute;left:170px;width:860px;top:281px;text-align:center;font-size:15.5px;line-height:26px;color:var(--white)}
.btn-demo{left:501px;top:377px;width:198px;height:46px;border-radius:23px;font-family:'Montserrat',sans-serif;font-size:18px}
.device{position:absolute;background:linear-gradient(135deg,#0c1b3d,#1f4fb0 55%,#5b7fd6);border:6px solid #2a2a2a}
.section-title{position:absolute;left:0;width:1200px;text-align:center;font-family:'Ubuntu',sans-serif;font-weight:700;color:var(--ink)}
.rule{position:absolute;height:3px;background:var(--navy)}
.photo-circle{position:absolute;border-radius:50%}
.ring{position:absolute;border-radius:50%;border:2px solid var(--ring)}
.svc-title{position:absolute;font-family:'Ubuntu',sans-serif;font-weight:700;font-size:42px;color:var(--navy)}
.svc-sub{position:absolute;font-family:'Ubuntu',sans-serif;font-weight:500;font-size:26px;color:#333}
.svc-text{position:absolute;width:559px;font-size:18.5px;line-height:25.6px;text-align:justify;color:var(--text)}
.btn-more{width:168px;height:45px;font-size:19px}
.about-band{position:absolute;background:var(--navy)}
.about-photo{position:absolute;left:0;top:2507px;width:597px;height:498px;background:linear-gradient(120deg,#d9dde3,#8d98a6 45%,#c9d6e6)}
.about-kicker{position:absolute;left:664px;top:2602px;font-family:'Ubuntu',sans-serif;font-weight:500;font-size:31px;color:var(--white)}
.about-title{position:absolute;left:664px;top:2655px;font-family:'Montserrat',sans-serif;font-weight:700;font-size:40px;color:var(--white)}
.about-text{position:absolute;left:664px;width:440px;font-size:13.5px;line-height:21.5px;color:var(--white)}
.testi-bg{position:absolute;left:0;top:3051px;width:1200px;height:600px;background:var(--soft)}
.card{position:absolute;top:3172px;width:318px;height:298px;background:var(--white)}
.card svg.corner{position:absolute;left:0;top:0}
.avatar{position:absolute;left:32px;top:31px;width:68px;height:68px;border-radius:50%;border:3px solid #fff;box-shadow:0 0 0 2px var(--navy);background:linear-gradient(160deg,#c9a587,#5e4a3f)}
.card-name{position:absolute;left:122px;top:42px;font-family:'Ubuntu',sans-serif;font-size:21px;color:var(--navy)}
.card-role{position:absolute;left:122px;top:70px;font-family:'Roboto Slab',serif;font-weight:300;font-size:13px;color:var(--muted)}
.card-text{position:absolute;left:43px;top:114px;width:260px;font-family:'Roboto Slab',serif;font-weight:300;font-size:13.5px;line-height:25.6px;color:var(--muted)}
.footer-bg{position:absolute;left:0;top:3420px}
.f-head{position:absolute;top:3658px;font-family:'Ubuntu',sans-serif;font-weight:500;font-size:26px;color:var(--white)}
.f-list{position:absolute;top:3719px;list-style:none;font-size:16px;color:var(--white)}
.f-list li{height:30px;line-height:22px}
.f-list li::before{content:"»";color:var(--red);margin-right:10px;font-weight:700}
.f-contact{position:absolute;left:592px;font-size:16px;line-height:26px;color:var(--white)}
.f-icon{position:absolute;left:556px}
.f-brand{position:absolute;left:846px;top:3700px;font-family:'Ubuntu',sans-serif;font-weight:700;font-size:54px;line-height:62px;color:var(--white)}
.f-rule{position:absolute;left:101px;top:3918px;width:998px;height:1px;background:#888}
.copy{position:absolute;left:0;width:1200px;top:3945px;text-align:center;font-size:14.5px;color:var(--white)}
</style>
</head>
<body>

<!-- Hero -->
<svg class="hero-bg" width="1200" height="1000" viewBox="0 0 1200 1000" aria-hidden="true">
  <path d="M0,0 H1200 V558 Q600,1000 0,590 Z" fill="var(--navy)"/>
</svg>
<div class="brand">Codeweave Orchard</div>
<div class="nav" style="left:383px">Home</div>
<div class="nav" style="left:454px">Product<span class="caret">&#9660;</span></div>
<div class="nav" style="left:552px">Features<span class="caret">&#9660;</span></div>
<div class="nav" style="left:656px">Integrations</div>
<div class="nav" style="left:774px">Security</div>
<div class="nav" style="left:864px">News</div>
<div class="btn btn-login">LOGIN</div>

<div class="hero-kicker">WELCOME TO</div>
<div class="hero-title">CODEWEAVE ORCHARD</div>
<p class="hero-text">Lorem ipsum dolor sit amet, consectetur adipiscing elit, sed do eiusmod tempor incididunt ut labore et dolore magna aliqua. Ut enim ad minim veniam, quis nostrud exercitation ullamco laboris nisi ut aliquip ex ea commodo consequat. Duis aute irure dolor in reprehenderit in voluptate velit esse cillum dolore eu fugiat nulla pariatur.</p>
<div class="btn btn-demo">REQUEST DEMO</div>

<div class="device" role="img" aria-label="Tablet showing the platform start screen" style="left:229px;top:527px;width:155px;height:228px;border-radius:10px"></div>
<div class="device" role="img" aria-label="Laptop showing the platform start screen" style="left:400px;top:462px;width:420px;height:300px;border-radius:10px 10px 0 0;border-bottom:0"></div>
<div class="abs" aria-hidden="true" style="left:333px;top:760px;width:558px;height:46px;background:linear-gradient(#c9c9cc,#8e8e93);border-radius:0 0 30px 30px"></div>
<div class="device" role="img" aria-label="Phone showing the platform start screen" style="left:825px;top:553px;width:90px;height:185px;border-radius:12px"></div>

<!-- Services -->
<h2 class="section-title" style="top:875px;font-size:42px">Our Services</h2>
<div class="rule" style="left:577px;top:929px;width:46px"></div>

<div class="ring" style="left:28px;top:1005px;width:406px;height:406px"></div>
<div class="photo-circle" role="img" aria-label="Couple receiving house keys from an adviser" style="left:70px;top:996px;width:396px;height:396px;background:linear-gradient(135deg,#8b6a55,#d4b79e 50%,#6d7a8c)"></div>
<h3 class="svc-title" style="left:543px;top:1022px">Applicant Orchard</h3>
<div class="svc-sub" style="left:546px;top:1085px">POS Definition</div>
<p class="svc-text" style="left:543px;top:1139px">Lorem ipsum dolor sit amet, consectetur adipiscing elit, sed do eiusmod tempor incididunt ut labore et dolore magna aliqua. Ut enim aA customizable, web based, point-of-sale application for borrowers to complete a loan application, and guide them through the mortgage process.d minim veniam, quis nostrud exercitation ullamco laboris nisi ut aliquip ex ea commodo consequat.</p>
<div class="btn btn-more" style="left:541px;top:1330px">Readr More</div>

<h3 class="svc-title" style="left:101px;top:1526px">Escrowmap Orchard</h3>
<div class="svc-sub" style="left:103px;top:1590px">LOS Definition</div>
<p class="svc-text" style="left:100px;top:1643px">A Mortgage Loan Origination System (LOS) is a platform that takes a completed loan application and facilitates the mortgage transaction from origination to post closing. LOS systems may include document management, pricing and eligibility engines, and compliance tools to decrease risk and increase loan manufacturing quality.</p>
<div class="btn btn-more" style="left:98px;top:1834px">Readr More</div>
<div class="ring" style="left:772px;top:1509px;width:406px;height:406px"></div>
<div class="photo-circle" role="img" aria-label="Hand passing house keys to another hand" style="left:738px;top:1501px;width:396px;height:396px;background:linear-gradient(135deg,#3b2a22,#b38e6e 50%,#e6ddd3)"></div>

<div class="ring" style="left:28px;top:2016px;width:406px;height:406px"></div>
<div class="photo-circle" role="img" aria-label="Couple looking at a phone beside a laptop" style="left:70px;top:2008px;width:396px;height:396px;background:linear-gradient(135deg,#5a4a40,#c8a48a 50%,#d9d9dc)"></div>
<h3 class="svc-title" style="left:543px;top:2033px">Dwelling Orchard</h3>
<div class="svc-sub" style="left:546px;top:2097px">POS Definition</div>
<p class="svc-text" style="left:543px;top:2150px">A customizable, web based, point-of-sale application for borrowers to complete a loan application, and guide them through the mortgage process. A customizable, web based, point-of-sale application for borrowers to complete a loan application, and guide them through the mortgage process. A customizable, web based, point-of-sale application .</p>
<div class="btn btn-more" style="left:541px;top:2342px">Readr More</div>

<!-- About -->
<div class="about-band" style="left:0;top:2552px;width:1200px;height:453px"></div>
<div class="about-band" style="left:141px;top:3005px;width:1059px;height:46px"></div>
<div class="about-photo" role="img" aria-label="Two business people shaking hands"></div>
<div class="about-kicker">About Us</div>
<div class="rule" style="left:664px;top:2640px;width:136px;height:2px;background:var(--white)"></div>
<h2 class="about-title">CODEWEAVE ORCHARD</h2>
<p class="about-text" style="top:2731px;font-weight:700">Lorem ipsum dolor sit amet, consectetur adipiscing elit, sed do eiusmod tempor incididunt ut labore et dolore magna aliqua. Ut enim ad minim veniam, quis nostrud exercitation ullamco laboris nisi ut aliquip ex ea commodo consequat. Duis aute irure dolor in reprehenderit in voluptate velit esse cillum dolore eu fugiat nulla pariatur.</p>
<p class="about-text" style="top:2861px">Lorem ipsum dolor sit amet, consectetur adipiscing elit, sed do eiusmod tempor incididunt ut labore et dolore magna aliqua. Ut enim ad minim veniam.</p>
<div class="btn btn-more" style="left:667px;top:2942px;width:166px">Readr More</div>

<!-- Testimonials -->
<div class="testi-bg"></div>
<h2 class="section-title" style="top:3090px;font-size:34px;color:var(--navy)">Testimonial</h2>

<div class="card" style="left:112px">
  <svg class="corner" width="318" height="220" aria-hidden="true"><polygon points="0,0 318,0 318,3 28,40 0,210" fill="var(--red)"/></svg>
  <div class="avatar" role="img" aria-label="Client portrait"></div>
  <div class="card-name">Marlo Vance</div>
  <div class="card-role">Lorem ipsum dolor</div>
  <p class="card-text">Sed ut perspiciatis unde omnis iste error sit voluptatem accusantium doloremque laudantium, totam rem aperiam, eaque ipsa quae ab illo inventore veritatis et quasi architecto beatae vitae dicta sunt explicabo.</p>
</div>
<div class="card" style="left:442px">
  <svg class="corner" width="318" height="220" aria-hidden="true"><polygon points="0,0 318,0 318,3 28,40 0,210" fill="var(--navy)"/></svg>
  <div class="avatar" role="img" aria-label="Client portrait"></div>
  <div class="card-name">Marlo Vance</div>
  <div class="card-role">Lorem ipsum dolor</div>
  <p class="card-text">Sed ut perspiciatis unde omnis iste error sit voluptatem accusantium doloremque laudantium, totam rem aperiam, eaque ipsa quae ab illo inventore veritatis et quasi architecto beatae vitae dicta sunt explicabo.</p>
</div>
<div class="card" style="left:772px">
  <svg class="corner" width="318" height="220" aria-hidden="true"><polygon points="0,0 318,0 318,3 28,40 0,210" fill="var(--red)"/></svg>
  <div class="avatar" role="img" aria-label="Client portrait"></div>
  <div class="card-name">Marlo Vance</div>
  <div class="card-role">Lorem ipsum dolor</div>
  <p class="card-text">Sed ut perspiciatis unde omnis iste error sit voluptatem accusantium doloremque laudantium, totam rem aperiam, eaque ipsa quae ab illo inventore veritatis et quasi architecto beatae vitae dicta sunt explicabo.</p>
</div>

<!-- Footer -->
<svg class="footer-bg" width="1200" height="576" viewBox="0 3420 1200 576" aria-hidden="true">
  <path d="M0,3645 Q600,3435 1200,3645 V3996 H0 Z" fill="#000"/>
  <path d="M0,3642 Q600,3430 1200,3642" fill="none" stroke="var(--navy)" stroke-width="7"/>
</svg>

<div class="f-head" style="left:116px">Quick link</div>
<ul class="f-list" style="left:106px">
  <li>Home</li><li>Product</li><li>Features</li><li>Integrations</li><li>Security</li><li>News</li>
</ul>
<div class="f-head" style="left:326px">Help Links</div>
<ul class="f-list" style="left:317px">
  <li>Terms &amp; Conditions</li><li>Privacy Policy</li><li>About Us</li><li>Support</li>
</ul>
<div class="f-head" style="left:557px">Contact Us</div>
<svg class="f-icon" style="top:3724px" width="14" height="18" viewBox="0 0 14 18" aria-hidden="true"><path d="M7,0 C3,0 0,3 0,7 C0,12 7,18 7,18 C7,18 14,12 14,7 C14,3 11,0 7,0 Z" fill="#fff"/><circle cx="7" cy="7" r="2.6" fill="#000"/></svg>
<div class="f-contact" style="top:3718px">253 Lorem ipsum dolor<br>eiusmod&nbsp; 1140</div>
<svg class="f-icon" style="top:3798px" width="15" height="15" viewBox="0 0 24 24" aria-hidden="true"><path d="M6.6,10.8 C8,13.6 10.4,16 13.2,17.4 L15.4,15.2 C15.7,14.9 16.1,14.8 16.4,15 C17.5,15.4 18.7,15.6 20,15.6 C20.6,15.6 21,16 21,16.6 V20 C21,20.6 20.6,21 20,21 C10.6,21 3,13.4 3,4 C3,3.4 3.4,3 4,3 H7.5 C8.1,3 8.5,3.4 8.5,4 C8.5,5.3 8.7,6.5 9.1,7.6 C9.2,7.9 9.1,8.3 8.9,8.6 Z" fill="#fff"/></svg>
<div class="f-contact" style="top:3793px">+ 1 555-014-2290</div>
<svg class="f-icon" style="top:3853px" width="17" height="13" viewBox="0 0 17 13" aria-hidden="true"><rect x="0.75" y="0.75" width="15.5" height="11.5" rx="1.5" fill="none" stroke="#fff" stroke-width="1.5"/><path d="M1,1 L8.5,7 L16,1" fill="none" stroke="#fff" stroke-width="1.5"/></svg>
<div class="f-contact" style="top:3846px">info@codeweaveorchard.com</div>

<div class="f-brand">Codeweave<br>Orchard</div>
<div class="f-rule"></div>
<div class="copy">Copyright © 2022 Codeweave Orchard - All Rights Reserved.</div>

</body>
</html>
```